Bref créative
Stationary, Envelope, and Business Card Designs for an Accounting/Bookkeeping company
R&K Ledger and Audit Partners, LLC
Professional
Doug M. Prentt
Partner, Chief Financial Officer
41207 Route 53
Maple Bend, FL 30417
dprentt@rkbooksco.com
www.rkbooksco.com
R&K Ledger and Audit Partners, LLC Logo in AI format - full color.
Logo color specifics.

```html
<!DOCTYPE html>
<html lang="en">
<head>
<meta charset="utf-8">
<title>R&amp;K Ledger and Audit Partners — Stationery Set</title>
<link href="https://fonts.googleapis.com/css2?family=Open+Sans:wght@400;600&display=swap" rel="stylesheet">
<style>
  :root{
    --bg:#ffffff;
    --paper:#ffffff;
    --brand-blue:#1f4f9e;
    --blue-deep:#16418c;
    --blue-light:#3f86cf;
    --accent-green:#6bb536;
    --ink:#4a5360;
    --ink-soft:#8a929c;
    --shadow:0 2px 6px rgba(0,0,0,.18);
  }
  *{margin:0;padding:0;box-sizing:border-box}
  html,body{width:1200px;height:936px;overflow:hidden;background:var(--bg)}
  .canvas{position:relative;width:1200px;height:936px;font-family:"Open Sans",Arial,sans-serif}
  .piece{position:absolute;background:var(--paper);box-shadow:var(--shadow);overflow:hidden}
  .piece svg.band{position:absolute;left:0;top:0;width:100%;height:100%}
  .brand{position:absolute;display:flex;align-items:center;gap:6px;color:var(--brand-blue);
    font-family:"Open Sans",Arial,sans-serif;font-weight:600;white-space:nowrap;line-height:1.2}
  .brand .dot{width:.8em;height:.8em;background:var(--brand-blue);flex:none}
  .contact{position:absolute;color:var(--ink-soft);line-height:1.55;white-space:nowrap}

  .letterhead{left:180px;top:46px;width:393px;height:568px}
  .letterhead .brand{left:22px;top:68px;font-size:10px}
  .letterhead .faint-mark{position:absolute;left:128px;top:210px;width:130px;height:130px;border-radius:50%;background:var(--brand-blue);opacity:.05}
  .letterhead .contact{left:22px;bottom:22px;font-size:6px}

  .folder{left:634px;top:38px;width:419px;height:579px}
  .folder .brand{left:0;right:0;top:272px;justify-content:center;font-size:17px;gap:9px}

  .card-front{left:43px;top:655px;width:185px;height:116px}
  .card-front .brand{left:10px;top:26px;font-size:6.5px;gap:4px}
  .card-front .contact{left:10px;top:58px;font-size:5px}
  .card-front .holder{position:absolute;right:10px;top:64px;text-align:right;color:var(--ink)}
  .card-front .holder b{display:block;font-size:6.5px;font-weight:600}
  .card-front .holder span{display:block;font-size:4.8px;color:var(--ink-soft)}

  .card-back{left:43px;top:786px;width:185px;height:107px}
  .card-back .brand{left:0;right:0;top:40px;justify-content:center;font-size:6.5px;gap:4px}
  .card-back .web{position:absolute;left:0;right:0;bottom:10px;text-align:center;font-size:5px;letter-spacing:2px;color:var(--ink-soft)}

  .env-front{left:264px;top:672px;width:436px;height:208px}
  .env-front .brand{left:16px;top:48px;font-size:8.5px;gap:5px}
  .env-front .contact{left:16px;top:80px;font-size:5.5px}

  .env-back{left:733px;top:672px;width:429px;height:208px}
  .env-back .web{position:absolute;left:0;right:0;top:14px;text-align:center;font-size:8px;letter-spacing:4px;color:#fff}
</style>
</head>
<body>
<main class="canvas">

  <section class="piece letterhead" aria-label="Letterhead">
    <svg class="band" viewBox="0 0 393 568" preserveAspectRatio="none" aria-hidden="true">
      <defs><linearGradient id="lhBlue" x1="0" x2="1"><stop offset="0" stop-color="var(--blue-light)"/><stop offset="1" stop-color="var(--blue-deep)"/></linearGradient></defs>
      <path d="M150,0 L393,0 L393,44 Z" fill="url(#lhBlue)"/>
      <line x1="0" y1="30" x2="393" y2="52" stroke="var(--accent-green)" stroke-width="1.5"/>
    </svg>
    <div class="brand"><span class="dot"></span>R&amp;K Ledger and Audit Partners, LLC</div>
    <div class="faint-mark"></div>
    <div class="contact">41207 Route 53<br>Maple Bend, FL 30417<br>Tel 555 010 2040<br>Fax 555 010 2041<br>dprentt@rkbooksco.com<br>www.rkbooksco.com</div>
  </section>

  <section class="piece folder" aria-label="Presentation folder">
    <svg class="band" viewBox="0 0 419 579" preserveAspectRatio="none" aria-hidden="true">
      <defs><linearGradient id="fdBlue" x1="0" x2="1"><stop offset="0" stop-color="var(--blue-light)"/><stop offset="1" stop-color="var(--blue-deep)"/></linearGradient></defs>
      <path d="M0,0 L419,0 L419,52 L0,8 Z" fill="url(#fdBlue)"/>
      <line x1="0" y1="20" x2="419" y2="64" stroke="var(--accent-green)" stroke-width="1.5"/>
    </svg>
    <div class="brand"><span class="dot"></span>R&amp;K Ledger and Audit Partners, LLC</div>
  </section>

  <section class="piece card-front" aria-label="Business card front">
    <svg class="band" viewBox="0 0 185 116" preserveAspectRatio="none" aria-hidden="true">
      <defs><linearGradient id="cfBlue" x1="0" x2="1"><stop offset="0" stop-color="var(--blue-light)"/><stop offset="1" stop-color="var(--blue-deep)"/></linearGradient></defs>
      <path d="M70,0 L185,0 L185,18 Z" fill="url(#cfBlue)"/>
      <line x1="40" y1="6" x2="185" y2="24" stroke="var(--accent-green)" stroke-width="1"/>
    </svg>
    <div class="brand"><span class="dot"></span>R&amp;K Ledger and Audit Partners, LLC</div>
    <div class="contact">41207 Route 53<br>Maple Bend, FL 30417<br>Tel 555 010 2040<br>dprentt@rkbooksco.com</div>
    <div class="holder"><b>Doug M. Prentt</b><span>Partner, Chief Financial Officer</span></div>
  </section>

  <section class="piece card-back" aria-label="Business card back">
    <div class="brand"><span class="dot"></span>R&amp;K Ledger and Audit Partners, LLC</div>
    <div class="web">www.rkbooksco.com</div>
  </section>

  <section class="piece env-front" aria-label="Envelope front">
    <svg class="band" viewBox="0 0 436 208" preserveAspectRatio="none" aria-hidden="true">
      <defs><linearGradient id="efBlue" x1="0" x2="1"><stop offset="0" stop-color="var(--blue-light)"/><stop offset="1" stop-color="var(--blue-deep)"/></linearGradient></defs>
      <path d="M170,0 L436,0 L436,38 Z" fill="url(#efBlue)"/>
      <line x1="120" y1="8" x2="436" y2="46" stroke="var(--accent-green)" stroke-width="1.5"/>
    </svg>
    <div class="brand"><span class="dot"></span>R&amp;K Ledger and Audit Partners, LLC</div>
    <div class="contact">41207 Route 53<br>Maple Bend, FL 30417</div>
  </section>

  <section class="piece env-back" aria-label="Envelope back">
    <svg class="band" viewBox="0 0 429 208" preserveAspectRatio="none" aria-hidden="true">
      <defs><linearGradient id="ebBlue" x1="0" x2="1"><stop offset="0" stop-color="var(--blue-deep)"/><stop offset=".5" stop-color="var(--blue-light)"/><stop offset="1" stop-color="var(--blue-deep)"/></linearGradient></defs>
      <rect x="0" y="0" width="429" height="38" fill="url(#ebBlue)"/>
      <path d="M0,38 L214,96 L429,38" fill="none" stroke="#d7dbe0" stroke-width="1"/>
      <path d="M0,208 L190,100 M429,208 L238,100" fill="none" stroke="#e4e7ea" stroke-width="1"/>
    </svg>
    <div class="web">WWW.RKBOOKSCO.COM</div>
  </section>

</main>
</body>
</html>
```